plumbing & gas fitting business card design

We need a business card design for a plumbing & gas fitting company. The company covers commercial, domestic and maintenance work. We would like a modern design communicating efficiency and sophistication. preferred colours would include (red grey & black) or (green grey & black). Please DO NOT include any water droplets.

Industry/Entity Type

Business

Contact Information for Business Card

Vortig Plumbing & Gas, Commercial Domestic & Maintenance, licence no. 617394K, ABN 47215830962, Phone 0417382956, Email vortigplumbingandgas@corvanet.com

```html
<!DOCTYPE html>
<html lang="en">
<head>
<meta charset="utf-8">
<title>Vortig Plumbing &amp; Gas — Business Card</title>
<link rel="stylesheet" href="https://fonts.googleapis.com/css2?family=Oswald:wght@500;600&family=Open+Sans:wght@400&display=swap">
<style>
  :root {
    --ink-top: #222222;
    --ink-bottom: #000000;
    --panel: #2e2e2e;
    --white: #ffffff;
    --red: #d81f26;
    --contact: #f2f2f2;
  }
  * { margin: 0; padding: 0; box-sizing: border-box; }
  html, body {
    width: 1200px;
    height: 741px;
    overflow: hidden;
    background: var(--ink-bottom);
  }
  .card {
    position: relative;
    width: 1200px;
    height: 741px;
    overflow: hidden;
  }
  .card-front {
    position: absolute;
    left: 0; top: 0;
    width: 965px;
    height: 741px;
    background: linear-gradient(180deg, var(--ink-top) 0%, #111111 45%, var(--ink-bottom) 100%);
  }
  .brand {
    position: absolute;
    left: 273px;
    top: 252px;
    width: 410px;
    display: flex;
    align-items: center;
    gap: 22px;
    font-family: "Oswald", sans-serif;
    font-weight: 600;
    color: var(--white);
    text-transform: uppercase;
  }
  .brand-mark {
    flex: 0 0 auto;
    width: 40px;
    height: 40px;
    background: var(--red);
  }
  .brand-name {
    display: flex;
    flex-direction: column;
    line-height: 1;
  }
  .brand-name-main {
    font-size: 112px;
    letter-spacing: 4px;
    line-height: 0.95;
  }
  .brand-name-sub {
    font-size: 48px;
    letter-spacing: 2px;
    margin-top: 10px;
  }
  .services {
    position: absolute;
    left: 135px;
    top: 664px;
    width: 690px;
    font-family: "Oswald", sans-serif;
    font-weight: 600;
    font-size: 44px;
    letter-spacing: 1px;
    color: var(--white);
    text-transform: uppercase;
    white-space: nowrap;
  }
  .contact-panel {
    position: absolute;
    left: 965px; top: 0;
    width: 235px;
    height: 741px;
    background: var(--panel);
  }
  .contact-line {
    position: absolute;
    writing-mode: vertical-rl;
    font-family: "Open Sans", sans-serif;
    font-weight: 400;
    font-size: 25px;
    color: var(--contact);
    white-space: nowrap;
    letter-spacing: 0.3px;
  }
  .contact-phone { left: 113px; top: 236px; }
  .contact-email { left: 81px; top: 63px; }
</style>
</head>
<body>
  <div class="card">
    <section class="card-front">
      <div class="brand">
        <span class="brand-mark"></span>
        <div class="brand-name">
          <span class="brand-name-main">Vortig</span>
          <span class="brand-name-sub">Plumbing &amp; Gas</span>
        </div>
      </div>
      <p class="services">Commercial, Domestic &amp; Maintenance</p>
    </section>
    <aside class="contact-panel">
      <p class="contact-line contact-phone">Phone: 0417382956</p>
      <p class="contact-line contact-email">Email: vortigplumbingandgas@corvanet.com</p>
    </aside>
  </div>
</body>
</html>
```